AWESOME CYBER MONDAY SALE AD NEEDED

Create a Cyber Monday ad for nitrile gloves. We are offering a box of 100, no-powder, exam grade nitrile gloves, for $9.99. No limit. Each case is $99. Create something simple, eye catching, cool. KelpTorch.com. Sale ends on December 4th. While supplies last. We are a local medical supply company in Hawaii that serves the general public in addition to local businesses, government, etc. Gloves are in short supply and we have tons of inventory ready to sell.

Target Market(s)

Businesses that use supplies such as gloves

Industry/Entity Type

medical supplies

Requirements
Must have
• The company logo, website, picture of gloves and pricing.

```html
<!DOCTYPE html>
<html lang="en">
<head>
<meta charset="utf-8">
<title>KelpTorch Cyber Monday Sale</title>
<link rel="stylesheet" href="https://fonts.googleapis.com/css2?family=Outfit:wght@900&family=Yellowtail&family=Kaushan+Script&family=Lato:ital,wght@0,300;0,400;0,700;0,900;1,900&family=Archivo+Black&display=block">
<style>
  :root {
    --page: #ffffff;
    --night: #0d0f3a;
    --deep-blue: #1a2c9c;
    --electric-blue: #2a7bd8;
    --violet: #5a2ea8;
    --neon-pink: #ff3d95;
    --hot-pink: #f0287c;
    --neon-cyan: #5fe3f2;
    --ink: #16161c;
    --lime: #a8d832;
    --leaf-green: #34a83a;
    --white: #ffffff;
    --photo-light: #eef1f4;
    --photo-mid: #cfd8e0;
  }
  * { margin: 0; padding: 0; box-sizing: border-box; }
  html, body { width: 1200px; height: 1000px; overflow: hidden; background: var(--page); }
  .canvas { position: relative; width: 1200px; height: 1000px; background: var(--page); }

  .ad {
    position: absolute; left: 162px; top: 64px; width: 876px; height: 878px; overflow: hidden;
    background:
      radial-gradient(ellipse 60% 35% at 55% 48%, rgba(120, 220, 255, 0.55), transparent 70%),
      radial-gradient(ellipse 50% 40% at 70% 20%, rgba(220, 80, 220, 0.45), transparent 70%),
      linear-gradient(180deg, var(--deep-blue) 0%, var(--violet) 22%, var(--electric-blue) 50%, #1b2a86 72%, var(--night) 100%);
  }
  .neon-frame { position: absolute; inset: 0; width: 100%; height: 100%; }

  .headline-cyber, .headline-monday {
    position: absolute; left: 0; width: 100%; text-align: center;
    font-family: "Outfit", sans-serif; font-weight: 900; letter-spacing: 4px; line-height: 1;
  }
  .headline-cyber { top: 16px; height: 200px; font-size: 196px; }
  .headline-cyber span { position: absolute; left: 0; top: 0; width: 100%; }
  .cyber-outline {
    color: var(--ink);
    text-shadow:
      7px 0 0 var(--ink), -7px 0 0 var(--ink), 0 7px 0 var(--ink), 0 -7px 0 var(--ink),
      5px 5px 0 var(--ink), -5px 5px 0 var(--ink), 5px -5px 0 var(--ink), -5px -5px 0 var(--ink),
      0 0 24px rgba(255, 61, 149, 0.9);
  }
  .cyber-fill {
    background: linear-gradient(180deg, transparent 0 22%, var(--neon-cyan) 22% 50%, var(--neon-pink) 50% 100%);
    -webkit-background-clip: text; background-clip: text;
    color: transparent; -webkit-text-fill-color: transparent;
  }
  .headline-monday {
    top: 196px; font-size: 154px; color: var(--ink);
    text-shadow:
      4px 0 0 var(--neon-pink), -4px 0 0 var(--neon-pink), 0 4px 0 var(--neon-pink), 0 -4px 0 var(--neon-pink),
      3px 3px 0 var(--neon-pink), -3px 3px 0 var(--neon-pink), 3px -3px 0 var(--neon-pink), -3px -3px 0 var(--neon-pink),
      0 0 20px rgba(255, 61, 149, 0.9);
  }
  .headline-sale {
    position: absolute; left: 272px; top: 290px; transform: rotate(-8deg);
    font-family: "Yellowtail", "Kaushan Script", cursive; font-size: 168px; color: var(--lime); line-height: 1;
    text-shadow:
      3px 0 0 var(--ink), -3px 0 0 var(--ink), 0 3px 0 var(--ink), 0 -3px 0 var(--ink),
      6px 6px 0 var(--ink);
  }

  .product-photo {
    position: absolute; left: 32px; top: 384px; width: 260px; height: 260px; border-radius: 50%;
    border: 12px solid var(--neon-cyan);
    box-shadow: inset 0 0 0 3px #7a3a6a;
    background: radial-gradient(circle at 50% 45%, var(--photo-light), var(--photo-mid));
  }

  .features {
    position: absolute; left: 308px; top: 444px; width: 520px; height: 142px;
    border-radius: 10px; padding: 14px 0 0 72px;
    background: linear-gradient(180deg, var(--neon-pink) 0%, var(--hot-pink) 70%, #b81d5e 100%);
    box-shadow: 0 0 20px rgba(255, 61, 149, 0.6);
    list-style: none;
  }
  .features li {
    display: flex; align-items: center; gap: 16px; height: 40px;
    font-family: "Lato", sans-serif; font-weight: 700; font-size: 28px; color: var(--white);
  }
  .features svg { width: 20px; height: 20px; flex: none; }

  .price {
    position: absolute; left: 373px; top: 592px; display: flex; align-items: baseline; gap: 10px;
    font-family: "Lato", sans-serif; color: var(--lime);
  }
  .price-for { font-weight: 900; font-size: 46px; }
  .price-amount {
    font-family: "Archivo Black", sans-serif; font-size: 116px; line-height: 1; letter-spacing: 3px;
    text-shadow: 6px 6px 0 var(--ink);
  }
  .terms {
    position: absolute; left: 374px; top: 704px;
    font-family: "Lato", sans-serif; font-weight: 400; font-size: 35px; color: var(--white);
  }
  .deadline {
    position: absolute; left: 375px; top: 772px; width: 453px; height: 40px; border-radius: 5px;
    background: var(--leaf-green); padding-left: 12px;
    font-family: "Lato", sans-serif; font-style: italic; font-weight: 900; font-size: 28px; line-height: 40px; color: var(--white);
  }
  .website {
    position: absolute; left: 374px; top: 820px;
    font-family: "Lato", sans-serif; font-size: 34px; color: var(--white);
  }
  .website-label { font-weight: 300; }
  .website-url { font-weight: 900; }

  .brand-name {
    position: absolute; left: 40px; top: 774px;
    font-family: "Lato", sans-serif; font-weight: 900; font-size: 56px; color: var(--white); letter-spacing: -1px;
  }
</style>
</head>
<body>
<main class="canvas">
  <section class="ad">
    <svg class="neon-frame" viewBox="0 0 876 878" aria-hidden="true">
      <defs>
        <filter id="glow" x="-20%" y="-20%" width="140%" height="140%">
          <feGaussianBlur stdDeviation="4" result="b"/>
          <feMerge><feMergeNode in="b"/><feMergeNode in="SourceGraphic"/></feMerge>
        </filter>
      </defs>
      <g fill="none" stroke="#e8f7ff" stroke-width="5" filter="url(#glow)">
        <polyline points="122,6 818,6 470,560"/>
        <line x1="122" y1="6" x2="470" y2="560"/>
        <line x1="0" y1="120" x2="300" y2="460" stroke-opacity="0.8"/>
        <line x1="876" y1="200" x2="640" y2="560" stroke-opacity="0.8"/>
      </g>
    </svg>

    <h1 class="headline-cyber"><span class="cyber-outline" aria-hidden="true">CYBER</span><span class="cyber-fill">CYBER</span></h1>
    <h2 class="headline-monday">MONDAY</h2>
    <p class="headline-sale">Sale</p>

    <div class="product-photo" role="img" aria-label="Hands pulling on blue nitrile exam gloves"></div>

    <ul class="features">
      <li><svg viewBox="0 0 20 20"><circle cx="10" cy="10" r="8" fill="none" stroke="#2a1030" stroke-width="1.6"/><path d="M6 10.5l3 3 6-7" fill="none" stroke="#2a1030" stroke-width="1.8"/></svg>A box of 100 pieces</li>
      <li><svg viewBox="0 0 20 20"><circle cx="10" cy="10" r="8" fill="none" stroke="#2a1030" stroke-width="1.6"/><path d="M6 10.5l3 3 6-7" fill="none" stroke="#2a1030" stroke-width="1.8"/></svg>No-powder gloves</li>
      <li><svg viewBox="0 0 20 20"><circle cx="10" cy="10" r="8" fill="none" stroke="#2a1030" stroke-width="1.6"/><path d="M6 10.5l3 3 6-7" fill="none" stroke="#2a1030" stroke-width="1.8"/></svg>Exam grade nitrile gloves</li>
    </ul>

    <p class="price"><span class="price-for">for</span><span class="price-amount">$9.99</span></p>
    <p class="terms">No limit. Each case is $99</p>
    <p class="deadline">Sale ends on December 4th</p>
    <p class="website"><span class="website-label">VISIT: </span><span class="website-url">KelpTorch.com</span></p>

    <p class="brand-name">kelptorch</p>
  </section>
</main>
</body>
</html>
```